Quick & Dirty Poster Design Project - A2 Posters

I run a business called Brindle Terrace. We sell high end outdoor flooring and walling (natural stone products) to architects and designers.

We work mainly with high end landscape designers on garden design and outdoor architecture.

Our sales teams provide advice and expertise and sell architectural design products to architects and designers.

I wanted to design some fun A2 posters to put in the sales offices just to create a bit of energy and momentum for staff. These are for internal use only.

The 4 copy lines are:

1.Beware of people who don't get their hands dirty

2. If you don't take a chance you won't have one

3. Having trouble getting started? Quit talking and start doing

4. Remember the questions you ask are more important than anything you could ever say

Just one copy line for each poster

(Pls note due to the limited budget and timings, I'm expecting interesting typeset posters not "designed" artworks). Thanks

Target Market(s)

sales team

Industry/Entity Type

Landscape

Requirements
Must have
• Our logo (Brindle Terrace) - I have provided a few versions of the logo
Nice to have
• Some design element alongside the typeface / copy

```html
<!DOCTYPE html>
<html lang="en">
<head>
<meta charset="utf-8">
<title>Brindle Terrace – Beware of people who don't get their hands dirty</title>
<link rel="stylesheet" href="https://fonts.googleapis.com/css2?family=Marcellus+SC&display=swap">
<style>
  :root {
    --page: #ffffff;
    --poster: #000000;
    --ink: #ffffff;
  }
  html, body {
    margin: 0;
    padding: 0;
    width: 1200px;
    height: 900px;
    overflow: hidden;
    background: var(--page);
  }
  .canvas {
    position: relative;
    width: 1200px;
    height: 900px;
    background: var(--page);
  }
  .poster {
    position: absolute;
    left: 298px;
    top: 20px;
    width: 579px;
    height: 827px;
    background: var(--poster);
    color: var(--ink);
    font-family: "Marcellus SC", "Trebuchet MS", sans-serif;
  }
  .headline {
    margin: 0;
    font-weight: 400;
  }
  .headline span {
    position: absolute;
    left: 0;
    width: 100%;
    text-align: center;
    line-height: 1;
    white-space: nowrap;
    padding-left: 18px;
    box-sizing: border-box;
  }
  .line-beware { top: 150px; font-size: 42px; letter-spacing: 2px; }
  .line-people { top: 200px; font-size: 100px; letter-spacing: 3px; }
  .line-who    { top: 292px; font-size: 64px; letter-spacing: 3px; }
  .line-get    { top: 338px; font-size: 196px; letter-spacing: 6px; }
  .line-hands  { top: 532px; font-size: 34px; letter-spacing: 3px; }
  .brand {
    position: absolute;
    right: 22px;
    bottom: 24px;
    display: flex;
    align-items: center;
    gap: 7px;
    font-size: 16px;
    letter-spacing: 1px;
    color: var(--ink);
  }
  .brand-dot {
    width: 14px;
    height: 14px;
    border-radius: 50%;
    background: var(--ink);
  }
</style>
</head>
<body>
  <div class="canvas">
    <section class="poster">
      <h1 class="headline">
        <span class="line-beware">Beware of</span>
        <span class="line-people">PEOPLE</span>
        <span class="line-who">WHO DON'T</span>
        <span class="line-get">GET</span>
        <span class="line-hands">THEIR HANDS DIRTY</span>
      </h1>
      <div class="brand">
        <span class="brand-dot"></span>
        <span class="brand-name">Brindle Terrace</span>
      </div>
    </section>
  </div>
</body>
</html>
```